Trifold flyer for our dental clinic (the Bright Harbor Clinic)

The goal of this project is to design a trifold flyer for our dental clinic (the Bright Harbor Clinic). The winning design is expected to be creative, artistic and coherent with our logo.
Updates

Designs look the same

Target Market(s)

Young generation with dental need.

Industry/Entity Type

Dental Clinic

Font styles to use
Sans Serif

Colors
0355a3
85acd3
85cae6
0592cd
00a990
86cfc6
cedeed
cee9f5
cfeae6

Requirements
Must have
• See the attached sketch for content arrangement.

```html
<!DOCTYPE html>
<html lang="en">
<head>
<meta charset="utf-8">
<title>Bright Harbor Clinic – Trifold Flyer</title>
<link href="https://fonts.googleapis.com/css2?family=Roboto+Condensed:ital,wght@0,400;0,700;1,400&display=swap" rel="stylesheet">
<style>
  :root {
    --navy: #0355a3;
    --sky: #7cbcf6;
    --sky-deep: #5aa6ec;
    --cyan: #0592cd;
    --teal-band: #79c4d0;
    --teal-photo: #5fb7bf;
    --mist: #cee9f5;
    --ice: #d8eef0;
    --offer-blue: #1a8fd6;
    --offer-dark: #0a4fa0;
    --ink: #3b3b3b;
    --white: #ffffff;
    --stage: #efefef;
  }
  * { box-sizing: border-box; margin: 0; padding: 0; }
  html, body { width: 1200px; height: 848px; overflow: hidden; }
  body {
    background: var(--stage);
    font-family: "Roboto Condensed", Arial, sans-serif;
    position: relative;
  }
  .flyer {
    position: absolute; left: 42px; top: 20px;
    width: 1116px; height: 808px;
    display: flex;
    box-shadow: 0 4px 18px rgba(0,0,0,.15);
  }
  .panel { position: relative; width: 372px; height: 808px; overflow: hidden; }

  /* ---------- Team panel ---------- */
  .panel-team { background: var(--sky); color: var(--white); }
  .team-watermark {
    position: absolute; left: -40px; top: 150px;
    transform: rotate(-38deg); transform-origin: left top;
    font-size: 78px; font-weight: 700; letter-spacing: 4px;
    color: var(--sky-deep); opacity: .55; white-space: nowrap;
  }
  .team-title {
    position: absolute; left: 18px; top: 70px;
    font-size: 27px; font-weight: 700; color: var(--ice);
  }
  .doctor { position: absolute; left: 38px; display: flex; gap: 14px; }
  .doctor-name { font-size: 14px; font-weight: 700; color: var(--navy); width: 28px; flex: none; }
  .body-copy {
    font-size: 12px; font-style: italic; line-height: 13.5px;
  }
  .panel-team .body-copy { color: var(--white); }
  .team-note { position: absolute; left: 38px; top: 460px; width: 290px; color: var(--navy) !important; }
  .team-photo {
    position: absolute; left: 0; top: 428px; width: 372px; height: 178px;
    background: linear-gradient(90deg, #dfe6ea, #f2f5f7 30%, #dfe6ea 55%, #f2f5f7 80%, #dfe6ea);
  }
  .team-extra-title { position: absolute; left: 14px; top: 624px; font-size: 14px; color: var(--white); }
  .team-extra { position: absolute; left: 38px; width: 290px; }

  /* ---------- Reviews panel ---------- */
  .panel-reviews { background: var(--white); }
  .reviews-band {
    position: absolute; left: 0; top: 22px; width: 262px; height: 48px;
    background: var(--teal-band); color: var(--white);
    font-size: 25px; font-weight: 700; padding: 8px 10px;
  }
  .review { position: absolute; left: 32px; width: 290px; }
  .review-name { font-size: 14px; color: var(--cyan); margin-bottom: 3px; }
  .review .body-copy { color: var(--ink); padding-left: 26px; }
  .reviews-photo {
    position: absolute; left: 0; top: 646px; width: 372px; height: 162px;
    background: linear-gradient(135deg, #c98a63, #e8b797 45%, #f4d2be 70%, #b9735a);
  }

  /* ---------- Cover panel ---------- */
  .panel-cover { background: var(--white); }
  .cover-photo {
    position: absolute; left: 0; top: 0; width: 372px; height: 428px;
    background: linear-gradient(120deg, #5db1b9, var(--teal-photo) 45%, #8fd0d3);
  }
  .call-arc { position: absolute; right: 0; top: 0; }
  .call {
    position: absolute; right: 14px; top: 30px; text-align: right; color: var(--navy);
    font-weight: 700;
  }
  .call-label { font-size: 18px; }
  .call-number { font-size: 28px; line-height: 1; }
  .brand {
    position: absolute; left: 0; top: 470px; width: 372px;
    display: flex; flex-direction: column; align-items: center; gap: 18px;
  }
  .brand-mark { width: 46px; height: 46px; border-radius: 50%; background: var(--cyan); }
  .brand-name { font-size: 30px; font-weight: 700; color: var(--cyan); letter-spacing: .5px; }
  .offers {
    position: absolute; left: 0; bottom: 0; width: 372px; height: 204px;
    background: var(--offer-blue); overflow: hidden; padding: 8px 14px;
  }
  .offers-swirl { position: absolute; inset: 0; }
  .offers-title { position: relative; font-size: 25px; font-weight: 700; color: var(--mist); margin-bottom: 10px; }
  .offer { position: relative; font-size: 23px; font-weight: 700; line-height: 37px; white-space: nowrap; }
  .offer-price { color: var(--white); }
  .offer-text { color: var(--offer-dark); font-size: 22px; }
</style>
</head>
<body>
<main class="flyer">

  <section class="panel panel-team">
    <div class="team-watermark" aria-hidden="true">BRIGHT HARBOR</div>
    <h2 class="team-title">Meet us!</h2>

    <div class="doctor" style="top:112px">
      <span class="doctor-name">Dr. A</span>
      <p class="body-copy" style="width:260px">dolor sit amet, consectetur adipiscing elit, sed do eiusmod tempor incididunt ut labore et dolore magna aliqua. Ut enim ad minim veniam, quis nostrud exercitation ullamco</p>
    </div>
    <div class="doctor" style="top:198px">
      <span class="doctor-name">Dr. A</span>
      <p class="body-copy" style="width:260px">dolor sit amet, consectetur adipiscing elit, sed do eiusmod tempor incididunt ut labore et dolore magna aliqua. Ut enim ad minim veniam, quis nostrud exercitation ullamco</p>
    </div>
    <div class="doctor" style="top:280px">
      <span class="doctor-name">Dr. A</span>
      <p class="body-copy" style="width:260px">dolor sit amet, consectetur adipiscing elit, sed do eiusmod tempor incididunt ut labore et dolore magna aliqua. Ut enim ad minim veniam, quis nostrud exercitation ullamco</p>
    </div>
    <p class="body-copy team-note" style="top:364px">dolor sit amet, consectetur adipiscing elit, sed do eiusmod tempor incididunt ut labore et dolore magna aliqua. Ut enim ad minim veniam, quis nostrud exercitation ullamco</p>

    <div class="team-photo" role="img" aria-label="Photo strip of three smiling dentists in white coats with arms crossed"></div>

    <h3 class="team-extra-title">Lorem ipsum</h3>
    <p class="body-copy team-extra" style="top:644px">dolor sit amet, consectetur adipiscing elit, sed do eiusmod tempor incididunt ut labore et dolore magna aliqua. Ut enim ad minim veniam, quis nostrud exercitation ullamco</p>
    <p class="body-copy team-extra" style="top:708px">dolor sit amet, consectetur adipiscing elit, sed do eiusmod tempor incididunt ut labore et dolore magna aliqua. Ut enim ad minim veniam, quis nostrud exercitation ullamco</p>
  </section>

  <section class="panel panel-reviews">
    <h2 class="reviews-band">Reviews</h2>
    <article class="review" style="top:88px">
      <h3 class="review-name">Lorem ipsum</h3>
      <p class="body-copy">dolor sit amet, consectetur adipiscing elit, sed do eiusmod tempor incididunt ut labore et dolore magna aliqua. Ut enim ad minim veniam, quis nostrud exercitation ullamco</p>
    </article>
    <article class="review" style="top:204px">
      <h3 class="review-name">Lorem ipsum</h3>
      <p class="body-copy">dolor sit amet, consectetur adipiscing elit, sed do eiusmod tempor incididunt ut labore et dolore magna aliqua. Ut enim ad minim veniam, quis nostrud exercitation ullamco</p>
    </article>
    <article class="review" style="top:322px">
      <h3 class="review-name">Lorem ipsum</h3>
      <p class="body-copy">dolor sit amet, consectetur adipiscing elit, sed do eiusmod tempor incididunt ut labore et dolore magna aliqua. Ut enim ad minim veniam, quis nostrud exercitation ullamco</p>
    </article>
    <article class="review" style="top:436px">
      <h3 class="review-name">Lorem ipsum</h3>
      <p class="body-copy">dolor sit amet, consectetur adipiscing elit, sed do eiusmod tempor incididunt ut labore et dolore magna aliqua. Ut enim ad minim veniam, quis nostrud exercitation ullamco</p>
    </article>
    <article class="review" style="top:558px">
      <h3 class="review-name">Lorem ipsum</h3>
      <p class="body-copy">dolor sit amet, consectetur adipiscing elit, sed do eiusmod tempor incididunt ut labore et dolore magna aliqua. Ut enim ad minim veniam, quis nostrud exercitation ullamco</p>
    </article>
    <div class="reviews-photo" role="img" aria-label="Close-up photo of a woman's bright smile"></div>
  </section>

  <section class="panel panel-cover">
    <div class="cover-photo" role="img" aria-label="Photo of a smiling young woman pointing upward against a teal backdrop"></div>
    <svg class="call-arc" width="240" height="140" viewBox="0 0 240 140" aria-hidden="true">
      <path d="M0 0 H240 V108 C180 140 90 130 40 70 C22 46 8 22 0 0 Z" fill="#8fd3e6"/>
      <path d="M20 0 H240 V96 C175 124 100 112 58 62 C42 42 28 22 20 0 Z" fill="#d8eef0"/>
    </svg>
    <div class="call">
      <div class="call-label">Call us now</div>
      <div class="call-number">55-210-4187</div>
    </div>

    <div class="brand">
      <span class="brand-mark" aria-hidden="true"></span>
      <span class="brand-name">BRIGHT HARBOR CLINIC</span>
    </div>

    <div class="offers">
      <svg class="offers-swirl" width="372" height="204" viewBox="0 0 372 204" aria-hidden="true">
        <path d="M150 0 C260 20 300 90 372 80 V0 Z" fill="#2a9de0"/>
        <path d="M372 120 C320 150 300 204 240 204 H372 Z" fill="#2a9de0"/>
      </svg>
      <h2 class="offers-title">Special Offers</h2>
      <p class="offer"><span class="offer-price">$69</span> <span class="offer-text">New Patien Special</span></p>
      <p class="offer"><span class="offer-price">$99</span> <span class="offer-text">In-office teeth whitening</span></p>
      <p class="offer"><span class="offer-price">25%-40% off</span> <span class="offer-text">on ClearTrack aligners</span></p>
    </div>
  </section>

</main>
</body>
</html>
```